Podcast website that will AMAZE

I need a Wordpress website designed for my podcast that I am about to launch. The podcast is called 'calm river bright lantern' and is targeted at 30-45 year old professional females. The podcast is aiming to provide listeners with information, from a variety of experts, to improve their health and well-being, but also their financial circumstances. I want a landing page that would appeal to this demographic that is clean and uncluttered. also, I want the ability to play the podcast episodes from the website by integrating with libsyn as the media host. I need the ability to capture their personal information and ability to provide downloadable documents to people who come to the website. Although I would not initially need a shopping cart I will need the ability to add one at a future date. I have attached the current logo to give you an idea of theme

Target Market(s)

30-45 year 0ld professional females with an interest in health

Coding

Coded - Design and coding required

Colors

Designer to choose colors to be used in the design.

Requirements
Must have
• - ability to play podcasts from website. will be using libsyn as media host
• - clean uncluttered layout
• - ability to capture emails from vistors
• - ability to include online store in the future

```html
<!DOCTYPE html>
<html lang="en">
<head>
<meta charset="utf-8">
<title>calm river bright lantern</title>
<link href="https://fonts.googleapis.com/css2?family=Poppins:wght@300;400;500;600&family=Open+Sans:wght@400;600&display=swap" rel="stylesheet">
<style>
:root{
  --purple:#8e3d96;
  --purple-soft:#c99bd0;
  --blue:#1e8fe6;
  --orange:#e07a1f;
  --ink:#1f1f1f;
  --muted:#444;
  --white:#fff;
  --teal-dark:#0f4d68;
  --footer:#0b0b0b;
}
*{box-sizing:border-box;margin:0;padding:0}
html,body{width:1200px;height:2956px;overflow:hidden;background:#fff}
body{position:relative;font-family:"Poppins",sans-serif;color:var(--ink)}
.abs{position:absolute}

/* hero */
.hero{left:0;top:0;width:1200px;height:656px;overflow:hidden;
  background:linear-gradient(100deg,#e7b978 0%,#b77a4a 25%,#6d4a3b 48%,#584a4e 70%,#3f3a44 100%)}
.hero-photo{left:0;top:0;width:1200px;height:656px;
  background:radial-gradient(ellipse 380px 300px at 160px 160px,rgba(255,226,170,.85),transparent 70%),
  radial-gradient(ellipse 240px 360px at 500px 330px,rgba(60,50,50,.55),transparent 70%)}
.brand{left:89px;top:30px;display:flex;align-items:center;gap:12px}
.brand-dot{width:34px;height:34px;border-radius:50%;background:var(--purple)}
.brand-name{font-family:"Poppins",sans-serif;font-weight:600;color:var(--purple);font-size:19px;line-height:22px;text-transform:uppercase;white-space:nowrap}
.nav{left:506px;top:40px;display:flex;gap:30px;font-family:"Open Sans",sans-serif;font-size:17px;color:#111;white-space:nowrap}
.nav .active{color:var(--purple)}
.search{left:932px;top:36px;width:182px;height:38px;border:2px solid #222;border-radius:20px;
  font-family:"Open Sans",sans-serif;font-size:14px;padding:9px 14px;color:#222}
.search svg{position:absolute;right:14px;top:11px}
.hero-copy{left:620px;top:270px;width:560px;text-align:center;color:#fff}
.hero-title{font-size:38px;font-weight:300;line-height:50px;white-space:nowrap}
.hero-sub{font-size:26px;font-weight:300;line-height:34px;margin-top:4px;white-space:nowrap}
.hero-dots{left:1155px;top:298px;display:flex;flex-direction:column;gap:10px}
.hero-dots span{width:8px;height:8px;border-radius:50%;background:#fff}
.hero-dots span:first-child{background:var(--purple-soft)}
.slider{left:0;top:518px;width:1200px;height:138px;background:rgba(25,22,24,.82)}
.slider-thumb{left:147px;top:540px;width:134px;height:96px;border-radius:4px;
  background:linear-gradient(135deg,#e8ddd2,#9bb27e 55%,#c0574a)}
.slider-title{left:309px;top:550px;font-size:17px;color:#fff;white-space:nowrap}
.slider-text{left:309px;top:580px;font-size:12px;line-height:22px;color:#ddd;width:560px;white-space:nowrap}
.btn-read{left:905px;top:568px;width:130px;height:38px;border-radius:20px;background:var(--blue);
  color:#fff;font-size:15px;text-align:center;line-height:38px}
.arrow{top:572px}

.arc{pointer-events:none}

/* podcasts */
.section-title{width:1200px;left:0;text-align:center;font-size:37px;font-weight:400;color:#111;white-space:nowrap}
.pod{width:305px;height:152px;border-radius:6px;overflow:hidden;color:#fff;
  background:linear-gradient(135deg,#2a2426,#5b4a40 55%,#1d1b1c)}
.pod.b{background:linear-gradient(135deg,#1e1a1b,#6b5444 50%,#2a2a28)}
.pod.c{background:linear-gradient(135deg,#1f2a1c,#50643e 55%,#1c1e18)}
.pod-title{position:absolute;left:24px;top:28px;font-size:19px;font-weight:500;white-space:nowrap}
.pod-meta{position:absolute;left:24px;top:52px;font-size:14px;white-space:nowrap}

/* about */
.about{left:0;top:1300px;width:1200px;height:483px;
  background:linear-gradient(100deg,#4a2a6a 0%,#3c3f78 40%,#1f6a85 75%,#1a7d8c 100%)}
.about-text{left:227px;top:1476px;width:746px;text-align:center;color:#fff;font-size:15px;line-height:32px}
.about-title{color:#fff}

/* store */
.product{width:317px}
.product-img{width:317px;height:191px;border:3px solid #eee;position:relative}
.price{position:absolute;right:0;bottom:0;background:var(--purple);color:#fff;font-size:18px;padding:7px 12px}
.product h3{font-weight:400;font-size:18px;margin:18px 0 10px 4px;white-space:nowrap}
.product p{font-size:13px;line-height:21px;color:#222;padding:0 4px}
.product a{display:block;margin-top:14px;font-size:13px;color:var(--orange);text-decoration:none}

/* newsletter */
.news{left:0;top:2388px;width:1200px;height:327px;
  background:radial-gradient(ellipse 400px 200px at 600px 180px,#1f6b86,transparent 80%),linear-gradient(180deg,#16607c,#0d4a63)}
.news-title{left:0;width:1200px;top:2466px;text-align:center;color:#fff;font-size:34px;font-weight:400;white-space:nowrap}
.news-text{left:0;width:1200px;top:2520px;text-align:center;color:#e6f0f4;font-size:15px;line-height:24px}
.news-form{left:355px;top:2593px;width:492px;height:40px;display:flex;border-radius:4px;overflow:hidden}
.news-form span{flex:1;background:#fff;font-size:13px;color:#777;padding:12px 14px}
.news-form b{width:81px;background:var(--purple);color:#fff;font-weight:400;font-size:14px;text-align:center;line-height:40px}

/* footer */
.footer{left:0;top:2715px;width:1200px;height:241px;background:var(--footer)}
.foot-nav{left:740px;top:2786px;display:flex;gap:28px;font-family:"Open Sans",sans-serif;font-size:16px;color:#fff;white-space:nowrap}
.copy{left:868px;top:2840px;font-family:"Open Sans",sans-serif;font-size:13px;color:#fff;white-space:nowrap}
.socials{left:111px;top:2848px;display:flex;gap:11px}
.socials span{width:30px;height:30px;border:2px solid #fff;border-radius:50%}
</style>
</head>
<body>

<!-- HERO -->
<section class="abs hero">
  <div class="abs hero-photo" role="img" aria-label="Woman running outdoors at sunset with mountains behind"></div>
</section>
<div class="abs brand">
  <span class="brand-dot"></span>
  <span class="brand-name">calm river<br>bright lantern</span>
</div>
<nav class="abs nav"><span class="active">Home</span><span>About</span><span>Podcasts</span><span>Store</span><span>Contact</span></nav>
<div class="abs search">Search
  <svg width="14" height="14" viewBox="0 0 14 14"><circle cx="6" cy="6" r="4.5" fill="none" stroke="#222" stroke-width="2"/><line x1="9.5" y1="9.5" x2="13" y2="13" stroke="#222" stroke-width="2"/></svg>
</div>
<div class="abs hero-copy">
  <h1 class="hero-title">calm river bright lantern</h1>
  <p class="hero-sub">Health and well-being</p>
</div>
<div class="abs hero-dots"><span></span><span></span><span></span></div>

<div class="abs slider"></div>
<svg class="abs arrow" style="left:88px" width="16" height="24" viewBox="0 0 16 24"><polyline points="13,3 4,12 13,21" fill="none" stroke="#fff" stroke-width="4"/></svg>
<svg class="abs arrow" style="left:1096px" width="16" height="24" viewBox="0 0 16 24"><polyline points="3,3 12,12 3,21" fill="none" stroke="#fff" stroke-width="4"/></svg>
<div class="abs slider-thumb" role="img" aria-label="Bowl of fresh salad"></div>
<p class="abs slider-title">Neque porro quisquam est qui dolorem ipsum</p>
<p class="abs slider-text">The point of using Lorem Ipsum is that it has a more-or-less normal distribution of letters.<br>It is a long established fact that a reader will be distracted by the readable</p>
<div class="abs btn-read">Read More</div>

<!-- corner arcs -->
<svg class="abs arc" style="left:0;top:656px" width="210" height="170" viewBox="0 0 210 170"><path d="M195 0 A190 190 0 0 1 0 150" fill="none" stroke="var(--purple)" stroke-width="22"/></svg>
<svg class="abs arc" style="left:1040px;top:1783px" width="160" height="200" viewBox="0 0 160 200"><path d="M15 0 A175 175 0 0 0 160 185" fill="none" stroke="var(--purple)" stroke-width="22"/></svg>

<!-- PODCASTS -->
<h2 class="abs section-title" style="top:752px">Play Podcasts</h2>

<div class="abs pod" style="left:116px;top:855px" role="img" aria-label="Podcast episode cover photo"></div>
<div class="abs pod b" style="left:451px;top:855px" role="img" aria-label="Podcast episode cover photo"></div>
<div class="abs pod c" style="left:784px;top:855px" role="img" aria-label="Podcast episode cover photo"></div>
<div class="abs pod c" style="left:116px;top:1030px" role="img" aria-label="Podcast episode cover photo"></div>
<div class="abs pod" style="left:451px;top:1030px" role="img" aria-label="Podcast episode cover photo"></div>
<div class="abs pod b" style="left:784px;top:1030px" role="img" aria-label="Podcast episode cover photo"></div>

<div class="abs" style="left:116px;top:855px;width:1000px;height:330px;color:#fff">
  <div class="abs" style="left:0;top:0;width:305px;height:152px"><span class="pod-title">PDC 19 – WAVEHALL</span><span class="pod-meta">LINDEN PLAY | 2017-11-11</span></div>
  <div class="abs" style="left:335px;top:0;width:305px;height:152px"><span class="pod-title">PDC 19 – WAVEHALL</span><span class="pod-meta">LINDEN PLAY | 2017-11-11</span></div>
  <div class="abs" style="left:668px;top:0;width:305px;height:152px"><span class="pod-title">PDC 19 – WAVEHALL</span><span class="pod-meta">LINDEN PLAY | 2017-11-11</span></div>
  <div class="abs" style="left:0;top:175px;width:305px;height:152px"><span class="pod-title">PDC 19 – WAVEHALL</span><span class="pod-meta">LINDEN PLAY | 2017-11-11</span></div>
  <div class="abs" style="left:335px;top:175px;width:305px;height:152px"><span class="pod-title">PDC 19 – WAVEHALL</span><span class="pod-meta">LINDEN PLAY | 2017-11-11</span></div>
  <div class="abs" style="left:668px;top:175px;width:305px;height:152px"><span class="pod-title">PDC 19 – WAVEHALL</span><span class="pod-meta">LINDEN PLAY | 2017-11-11</span></div>
</div>

<svg width="0" height="0" style="position:absolute">
  <defs>
    <g id="player">
      <circle cx="14" cy="15" r="13" fill="#fff"/>
      <polygon points="10,9 20,15 10,21" fill="var(--blue)"/>
      <line x1="38" y1="15" x2="232" y2="15" stroke="#fff" stroke-width="3"/>
      <circle cx="41" cy="15" r="5" fill="#fff"/>
      <polygon points="244,11 249,11 255,6 255,24 249,19 244,19" fill="#fff"/>
    </g>
  </defs>
</svg>
<svg class="abs" style="left:140px;top:950px" width="262" height="30"><use href="#player"/></svg>
<svg class="abs" style="left:475px;top:950px" width="262" height="30"><use href="#player"/></svg>
<svg class="abs" style="left:808px;top:950px" width="262" height="30"><use href="#player"/></svg>
<svg class="abs" style="left:140px;top:1125px" width="262" height="30"><use href="#player"/></svg>
<svg class="abs" style="left:475px;top:1125px" width="262" height="30"><use href="#player"/></svg>
<svg class="abs" style="left:808px;top:1125px" width="262" height="30"><use href="#player"/></svg>

<!-- ABOUT -->
<section class="abs about" role="img" aria-label="Soft purple to teal tinted photo backdrop"></section>
<h2 class="abs section-title about-title" style="top:1394px">About us</h2>
<p class="abs about-text">The point of using Lorem Ipsum is that it has a more-or-less normal distribution of letters, as opposed to using 'Content here, content here', making it look like readable English. Many desktop publishing packages and web page editors now use Lorem Ipsum as their default model text, and a search for 'lorem ipsum' will uncover many web sites still in their infancy</p>
<svg class="abs" style="left:166px;top:1638px" width="880" height="60" viewBox="0 0 880 60">
  <polygon points="2,2 22,15 2,28" fill="#fff"/>
  <text x="48" y="19" fill="#fff" font-size="9" font-family="Poppins,sans-serif">00:00</text>
  <line x1="90" y1="15" x2="746" y2="15" stroke="#fff" stroke-width="6" stroke-linecap="round"/>
  <text x="756" y="19" fill="#fff" font-size="9" font-family="Poppins,sans-serif">00:00</text>
  <polygon points="792,11 797,11 803,6 803,24 797,19 792,19" fill="#fff"/>
  <line x1="818" y1="15" x2="866" y2="15" stroke="#fff" stroke-width="5" stroke-linecap="round"/>
  <rect x="820" y="50" width="10" height="9" fill="none" stroke="#fff" stroke-width="1.5"/>
  <circle cx="851" cy="55" r="5" fill="#fff"/>
</svg>

<!-- STORE -->
<h2 class="abs section-title" style="top:1876px">Online Store</h2>
<article class="abs product" style="left:87px;top:1968px">
  <div class="product-img" role="img" aria-label="Pink cosmetic bottle with blossoms" style="background:linear-gradient(135deg,#f6c8d4,#e8899f 60%,#f4b6c6)"><span class="price">$49.00</span></div>
  <h3>Neque porro quisquam</h3>
  <p>It has survived not only five centuries, but also the leap into electronic typesetting.</p>
  <a>Read More »</a>
</article>
<article class="abs product" style="left:439px;top:1968px">
  <div class="product-img" role="img" aria-label="Jar of cream on green leaves" style="background:linear-gradient(135deg,#3d7a2c,#8a6a3a 55%,#4f5a3a)"><span class="price">$49.00</span></div>
  <h3>Dolorem ipsum quia</h3>
  <p>It has survived not only five centuries, but also the leap into electronic typesetting, remaining</p>
  <a>Read More »</a>
</article>
<article class="abs product" style="left:792px;top:1968px">
  <div class="product-img" role="img" aria-label="Spa oils, towel and bamboo" style="background:linear-gradient(135deg,#f3f1e6,#c8c36a 55%,#8fa93e)"><span class="price">$49.00</span></div>
  <h3>Ipsum quia dolor sit amet,</h3>
  <p>It has survived not only five centuries, but also the leap into electronic typesetting, remaining</p>
  <a>Read More »</a>
</article>

<!-- NEWSLETTER -->
<section class="abs news" role="img" aria-label="Deep teal tinted backdrop photo"></section>
<h2 class="abs news-title">Subscribe to Our Newsletter</h2>
<p class="abs news-text">Sed velit sapien, commodo et dictum porta, varius id nibh.<br>Vivamus sed sapien molestie maximus lorem ut commodo enim.</p>
<div class="abs news-form"><span>Your email address</span><b>Subscribe</b></div>

<!-- FOOTER -->
<footer class="abs footer"></footer>
<div class="abs brand" style="left:111px;top:2776px">
  <span class="brand-name" style="color:#fff">calm river<br>bright lantern</span>
</div>
<div class="abs socials"><span></span><span></span><span></span><span></span><span></span></div>
<nav class="abs foot-nav"><span>Home</span><span>About</span><span>Podcasts</span><span>Store</span><span>Contact</span></nav>
<p class="abs copy">Copyright © 2018 All Rights Reserved</p>

</body>
</html>
```